Start-up Cleaning Business Needs Professional Business Cards

Marta's Butler Cleaning, LLC, is a start-up business based in the Northern Virginia suburbs of Washington, DC. MBC provides cleaning and housekeeping services for homes and offices. We have three core values:

1. We are personal. We value knowing and being known by our customers and each other. If you want nameless, faceless service, you should choose another provider. We put "personal" at the front of the list, because it is most important to us; the design we choose will convey this value.

2. Like a hotel concierge, we are professional in attitude, posture, communication and processes.

3. Like a hotel concierge, we solve problems with a can-do attitude and never make excuses.

Our uniforms are khaki pants with pink polo shirts.

Our logo is attached. There are other symbols, not represented in our logo, that may convey our values well, such as a top hat and bow tie, magnifying glass, desk bell, etc.

Please include fields for an individual's name and title, office phone number, mobile phone number, email address and website address (www.martasbutlercleaning.example).

Standard U.S. size: 2" x 3.5"
Updates

I should have mentioned that the purpose of all our advertising - business cards included - is to motivate potential customers to call or email to arrange a free in-home estimate.

```html
<!DOCTYPE html>
<html lang="en">
<head>
<meta charset="utf-8">
<title>Marta's Butler Cleaning – Business Card</title>
<link rel="stylesheet" href="https://fonts.googleapis.com/css2?family=Open+Sans:wght@400;700&display=swap">
<style>
  :root {
    --stage: #7a8494;
    --card-white: #ffffff;
    --card-fade: #ececec;
    --card-dark: #3b3b3c;
    --card-dark-edge: #2a2a2b;
    --ink: #262626;
    --pink: #c91f7e;
    --plum: #a3437f;
    --maroon: #3a2224;
    --slate: #4a4a4c;
    --mist: #bdbdbd;
  }
  * { box-sizing: border-box; margin: 0; padding: 0; }
  html, body { width: 1200px; height: 1024px; overflow: hidden; }
  body {
    background: var(--stage);
    font-family: "Open Sans", Arial, sans-serif;
    position: relative;
  }
  .card {
    position: absolute;
    left: 250px;
    width: 700px;
    height: 400px;
    border-radius: 22px;
    overflow: hidden;
    box-shadow: 0 10px 28px rgba(0,0,0,0.35);
  }
  .card-back {
    top: 70px;
    background: linear-gradient(135deg, #474748 0%, var(--card-dark) 50%, var(--card-dark-edge) 100%);
  }
  .card-back .mascot-faint {
    position: absolute;
    left: 250px; top: 80px;
    width: 200px; height: 240px;
    border-radius: 40px;
    background: radial-gradient(ellipse at center, rgba(120,90,110,0.55) 0%, rgba(70,60,66,0.25) 60%, rgba(59,59,60,0) 100%);
  }
  .card-front {
    top: 554px;
    background: linear-gradient(160deg, var(--card-white) 0%, var(--card-white) 55%, var(--card-fade) 100%);
  }
  .colour-strip {
    position: absolute;
    left: 0; top: 0;
    width: 40px; height: 100%;
    display: flex; flex-direction: column;
  }
  .colour-strip span { flex: 1; }
  .colour-strip .b1 { background: var(--slate); }
  .colour-strip .b2 { background: var(--maroon); }
  .colour-strip .b3 { background: var(--pink); }
  .colour-strip .b4 { background: var(--plum); }
  .colour-strip .b5 { background: var(--mist); }
  .mascot {
    position: absolute;
    left: 330px; top: 38px;
    width: 270px; height: 150px;
    border-radius: 14px;
    background: linear-gradient(90deg, #f4dbe8 0%, #e8a8c8 50%, #f3e3eb 100%);
  }
  .brand {
    position: absolute;
    left: 84px; top: 96px;
    width: 220px;
    color: var(--ink);
    font-size: 22px;
    font-weight: 400;
    line-height: 1.3;
  }
  .divider {
    position: absolute;
    left: 360px; top: 212px;
    width: 290px; height: 2px;
    background: var(--pink);
  }
  .holder-name {
    position: absolute;
    left: 360px; top: 226px;
    font-size: 26px; font-weight: 700; color: var(--ink);
  }
  .contacts {
    position: absolute;
    left: 360px; top: 274px;
    list-style: none;
    font-size: 16px; color: var(--ink);
  }
  .contacts li {
    display: flex; align-items: center; gap: 10px;
    height: 26px;
    white-space: nowrap;
  }
  .contacts svg { width: 14px; height: 14px; fill: var(--pink); flex: none; }
</style>
</head>
<body>
  <div class="card card-back">
    <div class="mascot-faint" role="img" aria-label="Faint mascot drawing of a cleaner with a mop"></div>
  </div>

  <div class="card card-front">
    <div class="colour-strip">
      <span class="b1"></span><span class="b2"></span><span class="b3"></span><span class="b4"></span><span class="b5"></span>
    </div>
    <div class="mascot" role="img" aria-label="Drawing of a cleaner in pink pushing a mop"></div>
    <div class="brand">Marta's Butler Cleaning</div>
    <div class="divider"></div>
    <div class="holder-name">Dana Reyes</div>
    <ul class="contacts">
      <li>
        <svg viewBox="0 0 16 16"><path d="M3 1h3l1.5 4-2 1.2a9 9 0 0 0 4.3 4.3L11 8.5l4 1.5v3a2 2 0 0 1-2 2C6.9 15 1 9.1 1 3a2 2 0 0 1 2-2z"/></svg>
        555-010-2040
      </li>
      <li>
        <svg viewBox="0 0 16 16"><path d="M4 0h8a1 1 0 0 1 1 1v14a1 1 0 0 1-1 1H4a1 1 0 0 1-1-1V1a1 1 0 0 1 1-1zm1 2v10h6V2zm3 11a1 1 0 1 0 0 2 1 1 0 0 0 0-2z"/></svg>
        555-010-2041
      </li>
      <li>
        <svg viewBox="0 0 16 16"><path d="M1 3h14v10H1zm1.5 1.5v.3L8 9l5.5-4.2v-.3zm0 2.2v4.8h11V6.7L8 11z"/></svg>
        info@martasbutlercleaning.example
      </li>
      <li>
        <svg viewBox="0 0 16 16"><circle cx="8" cy="8" r="7"/><path d="M1 8h14M8 1c3 3 3 11 0 14M8 1c-3 3-3 11 0 14" stroke="#fff" stroke-width="1.2" fill="none"/></svg>
        www.martasbutlercleaning.example
      </li>
    </ul>
  </div>
</body>
</html>
```